Business Card Re-Design for a Lighting Designer

I would like my business card re-designed. It is currently high gloss and they scratch too easily. I don not think the current design lends itself well to a matte finish. I have included the current design for reference along with our company logo.
Check out our website for current branding.
http://www.brambleorchidstudio.example

Updates
Some of the top contenders are muslim and it is a holiday for them. I do not want to discriminate and would expect the same courtesy for holidays we celebrate.
Target Market(s)
Interior Designers, Architects
Contact Information for Business Card
Logo - Name, Title, Address, Telephone Number and Extension, Email
Font styles to use
Requirements
Must have
- All the information listed on the current business card. If you use Red, it needs to be the red from our logo.
Nice to have
- Vertical and Horizontal Designs will be entertained.
Should not have
- Requirements for a glossy finish...should not look too corporate since we are a design firm.

```html
<!DOCTYPE html>
<html lang="en">
<head>
<meta charset="utf-8">
<title>Bramble Orchid Studio – Business Card</title>
<link href="https://fonts.googleapis.com/css2?family=Montserrat:wght@400;500;700&display=swap" rel="stylesheet">
<style>
  :root {
    --backdrop: #2b2d31;
    --brand-red: #a3191f;
    --brand-red-deep: #941519;
    --paper-white: #ffffff;
    --logo-grey: #b9b9b9;
    --ink-red: #a3191f;
  }
  * { margin: 0; padding: 0; box-sizing: border-box; }
  html, body {
    width: 1200px;
    height: 900px;
    overflow: hidden;
    background: var(--backdrop);
  }
  .canvas {
    width: 1200px;
    height: 900px;
    display: flex;
    align-items: center;
    justify-content: center;
    gap: 40px;
    font-family: "Montserrat", sans-serif;
  }
  .card {
    position: relative;
    width: 540px;
    height: 309px;
    background: var(--brand-red);
    overflow: hidden;
  }

  /* Front: identity side */
  .card-front {
    display: flex;
    align-items: center;
    justify-content: center;
  }
  .identity {
    display: flex;
    align-items: center;
    gap: 16px;
  }
  .identity-square {
    width: 46px;
    height: 46px;
    background: var(--logo-grey);
  }
  .identity-name {
    color: var(--logo-grey);
    font-weight: 500;
    font-size: 26px;
    letter-spacing: 1px;
    line-height: 1.1;
    text-transform: uppercase;
  }

  /* Back: contact side */
  .artwork-area {
    position: absolute;
    inset: 0;
    background: linear-gradient(135deg, var(--brand-red) 0%, var(--brand-red-deep) 100%);
  }
  .white-band {
    position: absolute;
    inset: 0;
    width: 100%;
    height: 100%;
  }
  .address {
    position: absolute;
    left: 22px;
    top: 118px;
    width: 160px;
    color: var(--ink-red);
    font-size: 9.5px;
    font-weight: 500;
    line-height: 1.55;
    letter-spacing: 0.4px;
    display: flex;
    gap: 6px;
  }
  .address svg { flex: none; margin-top: 2px; }
  .person {
    position: absolute;
    left: 274px;
    top: 138px;
    width: 140px;
    text-align: center;
    color: var(--paper-white);
    white-space: nowrap;
  }
  .person-name {
    font-size: 10.5px;
    font-weight: 700;
    letter-spacing: 0.6px;
  }
  .person-title {
    font-size: 8px;
    font-weight: 400;
    letter-spacing: 1.8px;
    margin-top: 3px;
  }
  .contact {
    position: absolute;
    left: 206px;
    top: 226px;
    list-style: none;
    color: var(--paper-white);
    font-size: 9.5px;
    letter-spacing: 0.5px;
    line-height: 1.75;
    white-space: nowrap;
  }
  .contact li { display: flex; align-items: center; gap: 8px; }
  .contact .web { font-weight: 700; letter-spacing: 0.3px; }
</style>
</head>
<body>
<main class="canvas">

  <section class="card card-front" aria-label="Card front">
    <div class="identity">
      <span class="identity-square"></span>
      <span class="identity-name">Bramble Orchid<br>Studio</span>
    </div>
  </section>

  <section class="card card-back" aria-label="Card back">
    <div class="artwork-area" role="img" aria-label="Perspective room-line illustration in white on red"></div>
    <svg class="white-band" viewBox="0 0 540 309" aria-hidden="true">
      <polygon points="0,0 150,0 200,309 0,309" fill="var(--paper-white)"/>
    </svg>

    <div class="address">
      <svg width="8" height="10" viewBox="0 0 8 10" aria-hidden="true">
        <path d="M4 0a4 4 0 0 1 4 4c0 3-4 6-4 6S0 7 0 4a4 4 0 0 1 4-4z" fill="var(--ink-red)"/>
        <circle cx="4" cy="4" r="1.4" fill="var(--paper-white)"/>
      </svg>
      <span>210 Larkspur Commons,<br>Suite 40 Fairhaven,<br>Oregon 97000 USA</span>
    </div>

    <div class="person">
      <div class="person-name">MAREN CASTELL</div>
      <div class="person-title">PRINCIPALE</div>
    </div>

    <ul class="contact">
      <li>
        <svg width="8" height="9" viewBox="0 0 8 9" aria-hidden="true"><rect x="1.5" y="0.5" width="5" height="8" rx="1" fill="none" stroke="var(--paper-white)"/></svg>
        555.014.2290
      </li>
      <li>
        <svg width="9" height="7" viewBox="0 0 9 7" aria-hidden="true"><rect x="0.5" y="0.5" width="8" height="6" fill="none" stroke="var(--paper-white)"/><path d="M0.5 0.5l4 3.2 4-3.2" fill="none" stroke="var(--paper-white)"/></svg>
        maren@brambleorchidstudio.example
      </li>
      <li class="web">
        <svg width="9" height="9" viewBox="0 0 9 9" aria-hidden="true"><circle cx="4.5" cy="4.5" r="4" fill="none" stroke="var(--paper-white)"/><line x1="0.5" y1="4.5" x2="8.5" y2="4.5" stroke="var(--paper-white)"/></svg>
        www.brambleorchidstudio.example
      </li>
    </ul>
  </section>

</main>
</body>
</html>
```